Design needed for Cover of Conference Brochure

We are a conference company that puts on several business conferences per year. We are putting together a new conference - the Brightpath Insight Forum, and our audience is UX practitioners and specialists, product designers, UX designers, etc.
We need a brochure cover created. We are looking for fresh design ideas and are open to varying color schemes - please just keep in mind that this is a conference for business professionals, and fonts and colors should reflect this. Only restriction is that we do have a general cover format that we follow - i.e. which text goes where. (I've attached samples from our other events to reference.) We also generally have a central image to each brochure - feel free to submit a few versions with different images... we want something that accurately represents UX. However, if the design is compelling enough, image might not be completely necessary. We are relatively flexible - we just want something sharp!
- Must include KLVO logo (see placing on sample event covers)
- Must include footer - see sample covers
- Red text in word document are notes to you the designer - not actual text meant to appear on the cover
This cover is standard 8x11, and will be used for web only, not print. I have attached a word doc that includes all of the text that you will need for the cover. We will need final version in PDF, jpeg, and PSD. Please message me with any questions or clarification.

```html
<!DOCTYPE html>
<html lang="en">
<head>
<meta charset="utf-8">
<title>Brightpath Insight Forum — Brochure Cover</title>
<link href="https://fonts.googleapis.com/css2?family=Anton&family=Lato:ital,wght@0,400;0,700;0,900;1,900&family=Roboto+Condensed:wght@700&display=swap" rel="stylesheet">
<style>
  :root{
    --blue:#0c5aa6;
    --blue-light:#1a6fc0;
    --blue-deep:#083f7a;
    --yellow:#fbb829;
    --red:#e0201b;
    --ink:#111;
    --paper:#ffffff;
    --ray:#eef0f3;
    --stage:#d9dbde;
    --hero-blue:#2a7fc8;
    --hero-purple:#9b4fb0;
    --hero-pink:#d81b60;
    --hero-orange:#f7941d;
    --hero-green:#2aa55a;
  }
  *{box-sizing:border-box;margin:0;padding:0}
  html,body{width:907px;height:1200px;overflow:hidden;background:var(--stage)}
  .cover{
    position:absolute;left:40px;top:62px;width:825px;height:1050px;
    background:repeating-conic-gradient(from 0deg at 38% 42%, var(--paper) 0deg 7deg, var(--ray) 7deg 14deg);
    overflow:hidden;font-family:"Lato",sans-serif;
    box-shadow:0 4px 14px rgba(0,0,0,.25);
  }
  .subtitle-band{
    position:absolute;left:0;top:133px;width:100%;height:63px;background:var(--yellow);
    display:flex;align-items:center;justify-content:center;
  }
  .subtitle{
    font-family:"Roboto Condensed",sans-serif;font-weight:700;color:var(--blue);
    font-size:23px;letter-spacing:.3px;padding-top:14px;
  }
  .title-banner{
    position:absolute;left:55px;top:6px;width:745px;height:132px;
    background:linear-gradient(180deg,var(--blue-light),var(--blue-deep));
    border-radius:18px;display:flex;align-items:center;justify-content:center;
    box-shadow:0 3px 6px rgba(0,0,0,.3);
  }
  .title{
    font-family:"Anton",sans-serif;color:var(--yellow);font-size:64px;
    letter-spacing:1px;text-shadow:0 2px 2px rgba(0,0,0,.25);
  }
  .hero{
    position:absolute;left:45px;top:210px;width:450px;height:450px;border-radius:50%;
    background:linear-gradient(135deg,var(--hero-blue) 0%,var(--hero-purple) 35%,var(--hero-pink) 55%,var(--hero-orange) 78%,var(--hero-green) 100%);
    opacity:.9;
  }
  .tab{
    position:absolute;right:0;background:linear-gradient(180deg,var(--blue-light),var(--blue-deep));
    border-radius:14px 0 0 14px;color:var(--yellow);font-weight:900;
    box-shadow:0 3px 5px rgba(0,0,0,.3);
  }
  .tab-date{top:388px;left:523px;height:84px;display:flex;align-items:center;justify-content:center;font-size:29px}
  .tab-venue{top:508px;left:523px;height:84px;display:flex;flex-direction:column;justify-content:center;align-items:flex-end;padding-right:38px;font-size:17px;font-weight:700;line-height:1.6}
  .highlights{position:absolute;left:34px;top:672px;width:745px;list-style:none}
  .highlights li{
    position:relative;padding-left:18px;color:var(--red);font-size:21.5px;line-height:1.3;margin-bottom:2px;
  }
  .highlights svg{position:absolute;left:0;top:7px}
  .ribbon{position:absolute;left:68px;top:838px;width:722px;height:80px;transform:rotate(1.2deg)}
  .ribbon-text{
    position:absolute;left:60px;top:0;width:600px;height:64px;display:flex;align-items:center;justify-content:center;
    font-weight:900;font-style:italic;font-size:29px;color:var(--yellow);white-space:nowrap;
  }
  .ribbon-text em{color:#fff;margin-left:8px}
  .register{
    position:absolute;left:0;top:922px;width:472px;height:105px;background:var(--yellow);
    border-radius:0 22px 22px 0;padding:6px 0 0 32px;
  }
  .register h2{color:var(--blue);font-size:28px;font-weight:900;margin-bottom:4px}
  .register p{color:var(--ink);font-size:21px;font-weight:700;line-height:1.3}
  .brand{
    position:absolute;left:668px;top:958px;display:flex;align-items:center;gap:8px;
    color:var(--blue);font-weight:900;font-size:26px;
  }
  .brand-square{width:26px;height:26px;background:var(--blue);border-radius:4px}
  .footer-band{position:absolute;left:0;bottom:0;width:100%;height:26px;background:linear-gradient(180deg,var(--blue-light),var(--blue-deep))}
</style>
</head>
<body>
<main class="cover">
  <div class="subtitle-band"><p class="subtitle">Design Compelling Experiences through Successful UX Strategy</p></div>
  <header class="title-banner"><h1 class="title">Brightpath Insight Forum</h1></header>

  <div class="hero" role="img" aria-label="Colourful wheel of UX disciplines around a user pictogram: interaction design, information architecture, visual design, functionality, usability, typography, user interface, content strategy"></div>

  <div class="tab tab-date">June 10-12, 2014</div>
  <div class="tab tab-venue"><span>Harborview Union Club &amp; Hotel</span><span>San Francisco, CA</span></div>

  <ul class="highlights">
    <li><svg width="14" height="14" viewBox="0 0 14 14"><path d="M1 8l4 4 8-11" fill="none" stroke="#0c5aa6" stroke-width="2.4"/></svg>Case Studies from Leading Brands on Executing an Effective UX Strategy</li>
    <li><svg width="14" height="14" viewBox="0 0 14 14"><path d="M1 8l4 4 8-11" fill="none" stroke="#0c5aa6" stroke-width="2.4"/></svg>Learn How UX-Driven Innovation Can Change Your Business</li>
    <li><svg width="14" height="14" viewBox="0 0 14 14"><path d="M1 8l4 4 8-11" fill="none" stroke="#0c5aa6" stroke-width="2.4"/></svg>Build a Successful UX Team that Operates Strategically</li>
    <li><svg width="14" height="14" viewBox="0 0 14 14"><path d="M1 8l4 4 8-11" fill="none" stroke="#0c5aa6" stroke-width="2.4"/></svg>Insights into UX Research, User Behavior, Usability Testing, Lean UX, and<br>More</li>
  </ul>

  <div class="ribbon">
    <svg width="722" height="80" viewBox="0 0 722 80">
      <path d="M0 14 H70 V74 H0 L26 44 Z" fill="#083f7a"/>
      <path d="M722 14 H652 V74 H722 L696 44 Z" fill="#083f7a"/>
      <rect x="52" y="0" width="618" height="64" fill="#0c5aa6"/>
    </svg>
    <div class="ribbon-text">Register by March 7th, 2014 and<em>save $400!</em></div>
  </div>

  <section class="register">
    <h2>Register Today!</h2>
    <p>http://www.brightpathinsightforum.com</p>
    <p>888.555.0142</p>
  </section>

  <div class="brand"><span class="brand-square"></span>KLVO</div>
  <div class="footer-band"></div>
</main>
</body>
</html>
```